zorvantix Web Design Project

It is a virtual assistance/concierge company that helps the busy professional by remotely providing administrative, technical and/or creative business support services, specializing in the medical device industry. Company name is zorvantix.
(website will be zorvantix.com)

Allowing things to be done without taking time away from more urgent issues or family/personal time. Partnering with a VA reduces stress, protects cash flow, eliminates administrative hassles, and enables business people to find the success they originally set out to achieve. Saves small businesses and/or individuals on overhead, salary, et. Work is done remotely to offer administrative, clerical, typing and specialist service assistance on a regular, ad-hoc or emergency cover basis.

Though we are capable of addressing the needs of medical professionals and industry representatives due to our experience and knowledge (sales, HCC guidelines, etc.) we do not want to be limited to that market only.

Target Market(s)

Target market would be M/F, 30-50, National, busy, Alpha, entrepreneurs and industry professionals who want/need to do more without sacrifice of life

Industry/Entity Type

Industry

Requirements
Nice to have
• We do have a logo designed via the MarqueLoom website that can/should be included. Logo is uploaded.

```html
<!DOCTYPE html>
<html lang="en">
<head>
<meta charset="utf-8">
<title>zorvantix — Virtual Assistance</title>
<link href="https://fonts.googleapis.com/css2?family=Ubuntu:wght@400;500&family=PT+Sans:wght@400;700&display=swap" rel="stylesheet">
<style>
:root{
  --red:#c8101c;
  --red-dark:#a9000e;
  --navy:#16324a;
  --ink:#3a3a3a;
  --muted:#555;
  --line:#dde2e8;
  --panel:#ffffff;
  --page:#eef1f5;
  --black:#050505;
}
*{margin:0;padding:0;box-sizing:border-box}
html,body{width:860px;height:1200px;overflow:hidden;background:#fff}
body{font-family:"PT Sans",Arial,sans-serif;color:var(--ink);position:relative}
.abs{position:absolute}
h1,h2,h3,.logo,.nav a{font-family:"Ubuntu",Arial,sans-serif;font-weight:400}

.topline{left:0;top:0;width:860px;height:3px;background:var(--navy)}
.utility{left:685px;top:4px;width:142px;height:27px;background:#eef0f3;border-radius:0 0 4px 4px;font-size:11.5px;color:var(--navy);display:flex;align-items:center;justify-content:center;gap:6px}
.logo{left:28px;top:42px;display:flex;align-items:center;gap:8px;font-size:36px;color:var(--navy);font-weight:500;letter-spacing:-0.5px}
.logo .mark{width:12px;height:12px;border-radius:50%;background:var(--red)}
.search{left:622px;top:66px;width:204px;height:24px;border:1px solid #b9c6d2;border-radius:4px;background:#fff;font-size:11px;font-style:italic;color:#8a96a3;padding:5px 9px}
.search svg{position:absolute;right:5px;top:4px}

.nav{left:26px;top:112px;width:815px;height:41px;background:linear-gradient(#dd1e27,var(--red-dark));border-radius:3px;display:flex}
.nav a{color:#fff;font-size:13px;text-decoration:none;display:flex;align-items:center;justify-content:center;border-right:1px solid #8e0010;box-shadow:1px 0 0 #e4454b}
.nav a:last-child{border:none;box-shadow:none}

.hero-bg{left:0;top:153px;width:860px;height:288px;background:linear-gradient(90deg,#f6f7f9 0%,#f1f3f6 40%,#e8ecf0 100%)}
.hero-photo{left:190px;top:153px;width:670px;height:288px;background:linear-gradient(90deg,rgba(240,242,245,0) 0%,#d8dfe6 25%,#b7c6d4 55%,#cfd8e2 100%)}
.hero-title{left:50px;top:204px;font-size:29px;line-height:34px;color:var(--red);white-space:nowrap}
.hero-sub{left:50px;top:237px;font-size:22px;line-height:28px;color:var(--navy);white-space:nowrap}
.hero-text{left:51px;top:275px;width:270px;font-size:10.5px;line-height:15px;color:var(--navy)}
.btn{left:51px;top:329px;width:77px;height:24px;background:var(--red);border-radius:3px;color:#fff;font-size:11px;display:flex;align-items:center;justify-content:center;gap:5px}
.dots{left:30px;top:417px;display:flex;gap:4px}
.dots span{width:10px;height:9px;background:#e6939a}
.dots span:first-child{background:var(--red)}

.band{left:0;top:441px;width:860px;height:176px;background:linear-gradient(#fff,var(--page))}
.features{left:22px;top:441px;width:811px;height:159px;background:var(--panel);border:1px solid #e4e8ec;border-radius:4px;display:flex}
.feature{flex:1;padding:0 0 0 29px;border-right:1px solid var(--line);margin:16px 0 14px}
.feature:last-child{border:none}
.feature h3{font-size:18px;color:var(--navy);display:flex;align-items:center;gap:8px;margin-bottom:10px;height:34px}
.feature p{font-size:10.3px;line-height:15px;width:222px}
.more{font-size:10.5px;color:var(--navy);margin-top:8px;display:block}

.main h2,.why h2{font-size:18px;color:var(--red)}
.welcome{left:23px;top:637px;width:530px}
.welcome p{font-size:10.2px;line-height:14.2px;color:var(--muted)}
.welcome p+p{margin-top:13px}
.rule{left:26px;top:842px;width:528px;height:1px;background:var(--line)}
.why{left:26px;top:860px;width:530px}
.why-img{left:25px;top:893px;width:144px;height:155px;border:3px solid #fff;box-shadow:0 0 0 1px #ccc;background:linear-gradient(135deg,#5cc1cf,#2a8ea3 55%,#d7dde2)}
.why-text{left:186px;top:890px;width:370px;font-size:10.2px;line-height:14.3px;color:var(--muted)}
.why-text .lead{color:var(--red)}
.why-text p+p{margin-top:9px}
.list{left:186px;top:999px;display:grid;grid-template-columns:176px 180px;row-gap:4px;font-size:10.6px;color:var(--red);font-family:"Ubuntu",sans-serif}
.list li{list-style:none;white-space:nowrap}
.list li::before{content:"›";margin-right:6px}

.side{left:579px;top:632px;width:258px;height:480px;border:1px solid #dfe3e8;border-radius:4px;background:#fff}
.side-title{font-size:16px;color:var(--red);padding:8px 13px;height:33px;border-bottom:1px solid var(--line);background:linear-gradient(#fff,#f3f5f8)}
.video{left:588px;top:676px;width:239px;height:153px;background:var(--black);border-radius:3px}
.news-head{left:580px;top:847px;width:256px;border-top:1px solid var(--line)}
.news{left:593px;top:890px;width:230px;font-size:10.2px;line-height:14px;color:var(--muted)}
.news .date{color:#111;font-size:10.8px;margin-bottom:5px}
.news .rm{color:#111;margin-top:5px}
.news .sep{border-top:1px dotted #999;margin:8px 0 12px}
.viewmore{left:768px;top:1090px;font-size:10.5px;color:var(--navy)}

.footer{left:0;top:1117px;width:860px;height:83px;background:linear-gradient(#eef1f5,#f7f8fa)}
.foot-links{left:20px;top:1133px;font-size:10px;color:var(--navy);word-spacing:2px}
.copy{left:20px;top:1160px;font-size:10px;color:var(--navy)}
</style>
</head>
<body>
<div class="abs topline"></div>
<div class="abs utility"><span>Faq</span>|<span>Login</span>|<span>Contact</span></div>
<div class="abs logo"><span class="mark"></span>zorvantix</div>
<div class="abs search">Search here
  <svg width="16" height="16" viewBox="0 0 16 16"><circle cx="6.5" cy="6.5" r="4.8" fill="none" stroke="#16324a" stroke-width="2"/><line x1="10" y1="10" x2="14.5" y2="14.5" stroke="#16324a" stroke-width="2.4" stroke-linecap="round"/></svg>
</div>

<nav class="abs nav">
  <a style="width:81px;font-weight:500">Main</a>
  <a style="width:91px;font-weight:500">About Us</a>
  <a style="width:86px;font-weight:500">Services</a>
  <a style="width:113px">Testimonials</a>
  <a style="width:91px">Projects</a>
  <a style="width:70px">Blog</a>
  <a style="width:91px">Support</a>
  <a style="width:90px">Contact</a>
</nav>

<section>
  <div class="abs hero-bg"></div>
  <div class="abs hero-photo" role="img" aria-label="Photo of smiling support staff wearing headsets at work"></div>
  <h1 class="abs hero-title">Best Technical Support</h1>
  <h2 class="abs hero-sub">to the Medical Industry</h2>
  <p class="abs hero-text">Nordavel eSolutions is a web service company, offering a wide range of services which range from designing and development, that is covering almost</p>
  <div class="abs btn">learn more <svg width="6" height="9" viewBox="0 0 6 9"><path d="M1 1l3.5 3.5L1 8" fill="none" stroke="#fff" stroke-width="1.6"/></svg></div>
  <div class="abs dots"><span></span><span></span><span></span><span></span></div>
</section>

<div class="abs band"></div>
<section class="abs features">
  <div class="feature">
    <h3><svg width="34" height="32" viewBox="0 0 34 32"><rect x="3" y="3" width="24" height="26" rx="3" fill="#e8eef2" stroke="#7aa33a" stroke-width="2"/><path d="M8 22c6 4 14 2 20-8" stroke="#c8101c" stroke-width="4" fill="none" stroke-linecap="round"/></svg>Technical Support</h3>
    <p>Nordavel eSolutions is a web service company, offering a wide range of services which range from designing and development, that is covering almost all the fields in the best possible way.</p>
    <span class="more">READ MORE &nbsp;›</span>
  </div>
  <div class="feature">
    <h3><svg width="34" height="34" viewBox="0 0 34 34"><circle cx="17" cy="17" r="15" fill="#2a6fbf"/><circle cx="13" cy="12" r="6" fill="#6fb3ec" opacity=".7"/></svg>Providing Assistant</h3>
    <p>Nordavel eSolutions is a web service company, offering a wide range of services which range from designing and development, that is covering almost all the fields in the best possible way.</p>
    <span class="more">READ MORE &nbsp;›</span>
  </div>
  <div class="feature">
    <h3><svg width="36" height="28" viewBox="0 0 36 28"><rect x="1" y="2" width="34" height="24" rx="2" fill="#f3f3f3" stroke="#b22" stroke-width="2" stroke-dasharray="4 3"/><path d="M2 4l16 12 16-12" fill="none" stroke="#888" stroke-width="1.5"/></svg>Featured Service</h3>
    <p>Nordavel eSolutions is a web service company, offering a wide range of services which range from designing and development, that is covering almost all the fields in the best possible way.</p>
    <span class="more">READ MORE &nbsp;›</span>
  </div>
</section>

<section class="abs welcome main">
  <h2 style="margin-bottom:10px">Welcome to Our Website Mainpage</h2>
  <p>Nordavel eSolutions is a web service company, offering a wide range of services which range from designing and development, that is covering almost all the fields in the best possible way. To be the best we know what and how to present beautifully the working of the client’s need and their advantages be highlighted. We act in accordance with the Industry certified processes to deliver the best to our clients all over the world.</p>
  <p>Thus, Wanna get ahead in the competition with other websites…. Nordavel esolutions provide you with an attractive and most convincing website to enhance your marketing goals.<br>The only way to success is through the right path and that’s what we provide you. None of the other companies has the result we do. So stick to the best that’s how you will be the best don’t opt for the second best. Our expertise does not limit itself to web development but also it includes Web Hosting, Search Engine Optimization, E-Commerce. We partner hundreds of organization to enhance their business, marketing and profit goals.</p>
</section>
<div class="abs rule"></div>

<section>
  <div class="abs why"><h2>Why We Are</h2></div>
  <div class="abs why-img" role="img" aria-label="Photo of a person wearing a futuristic visor with digital displays"></div>
  <div class="abs why-text">
    <p><span class="lead">Nordavel eSolutions is a web service company, offering a wide range of services which range from designing and development,</span> that is covering almost all the fields in the best possible way.</p>
    <p>To be the best we know what and how to present beautifully the working of the client’s need and their advantages be highlighted. We act in accordance with the Industry certified processes to deliver the best to our clients all over the world.</p>
  </div>
  <ul class="abs list">
    <li>Your featured services goes here</li><li>Your featured services goes here</li>
    <li>featured services goes here</li><li>featured services goes here</li>
    <li>Your featured services goes here</li><li>Your featured goes here</li>
    <li>Your featured services goes here</li><li>Your featured services goes here</li>
  </ul>
</section>

<aside class="abs side"><h2 class="side-title">Latest Video</h2></aside>
<div class="abs video">
  <svg width="239" height="153" viewBox="0 0 239 153"><circle cx="114" cy="69" r="16" fill="none" stroke="#fff" stroke-width="2.5"/><path d="M109 61v16l13-8z" fill="#fff"/><line x1="12" y1="136" x2="228" y2="136" stroke="#bbb" stroke-width="1"/><circle cx="26" cy="136" r="3.5" fill="#fff"/></svg>
</div>
<div class="abs news-head"><h2 class="side-title">Latest News</h2></div>
<div class="abs news">
  <div class="date">20.March.2012</div>
  <p>The companies with fewer budgets can promote their products and services through the static website and gain a lot.</p>
  <p class="rm">read more</p>
  <div class="sep"></div>
  <div class="date">10.March.2012</div>
  <p>Nordavel eSolutions is specialized in handling advanced web projects and the ongoing projects that require permanent maintenance and support .We</p>
  <p class="rm">read more</p>
</div>
<div class="abs viewmore">VIEW MORE</div>

<footer>
  <div class="abs footer"></div>
  <div class="abs foot-links">Main &nbsp;| &nbsp;About Us &nbsp;| &nbsp;Services &nbsp;| &nbsp;Testimonials &nbsp;| &nbsp;Projects &nbsp;| &nbsp;Blog &nbsp;| &nbsp;Support &nbsp;| &nbsp;Contact</div>
  <div class="abs copy">© 2012 Company Name &nbsp;| &nbsp;All right reserved</div>
</footer>
</body>
</html>
```